need a Flyer for Plush Toy company

Need a Flyer for Plush Toy company ,

I upload a file for TEXT

Target Market(s)

Toys wholesalers , Supermarket

Industry/Entity Type

Toy Store

Colors
000000
ec1f27
c4c4c4

Requirements
Must have
• I have up loaded 3 files
• 1. Logo Registered Brand
• 2. customer's design in drawing
• 3. our ready samples based on Design
Nice to have
• happy kids in Nature ,
• happy kids in Ski ,
• different color Kids ,
• Multi culture concept

```html
<!DOCTYPE html>
<html lang="en">
<head>
<meta charset="utf-8">
<title>Seafolk Toys – Have you been there?</title>
<link rel="stylesheet" href="https://fonts.googleapis.com/css2?family=Delius&display=swap">
<style>
  :root {
    --paper: #ffffff;
    --sea-deep: #2fa9bf;
    --sea-mid: #7fcbd8;
    --sea-pale: #cfeaf0;
    --sea-mist: #e9f6f8;
    --sofa-green: #9cc79a;
    --plush-cream: #f3ece0;
    --brand-black: #000000;
    --brand-red: #c7262b;
  }
  * { margin: 0; padding: 0; box-sizing: border-box; }
  html, body {
    width: 1200px;
    height: 814px;
    overflow: hidden;
    background: var(--paper);
  }
  .flyer {
    position: relative;
    width: 1200px;
    height: 814px;
    overflow: hidden;
    background: var(--paper);
    font-family: "Delius", cursive;
  }
  .flyer__sea {
    position: absolute;
    inset: 0;
    width: 1200px;
    height: 814px;
  }
  .flyer__sofa-photo {
    position: absolute;
    left: 64px;
    top: 332px;
    width: 543px;
    height: 220px;
    border-radius: 14px 14px 4px 4px;
    background: linear-gradient(180deg, var(--plush-cream) 0%, #e7e3f0 30%, var(--sofa-green) 45%, #88b886 100%);
  }
  .flyer__sofa-reflection {
    position: absolute;
    left: 64px;
    top: 570px;
    width: 543px;
    height: 150px;
    background: linear-gradient(180deg, rgba(156, 199, 154, 0.45) 0%, rgba(156, 199, 154, 0) 100%);
  }
  .brand {
    position: absolute;
    left: 830px;
    top: 130px;
    width: 290px;
    text-align: center;
  }
  .brand__mark {
    display: flex;
    align-items: center;
    justify-content: center;
    gap: 12px;
    height: 180px;
  }
  .brand__dot {
    width: 22px;
    height: 22px;
    border-radius: 50%;
    background: var(--brand-black);
  }
  .brand__name {
    font-size: 34px;
    color: var(--brand-black);
    font-weight: 400;
  }
  .brand__tagline {
    margin-top: 4px;
    font-size: 29px;
    color: var(--brand-red);
    letter-spacing: 0.2px;
  }
</style>
</head>
<body>
<main class="flyer">
  <svg class="flyer__sea" viewBox="0 0 1200 814" aria-hidden="true">
    <defs>
      <linearGradient id="panelFade" x1="0" y1="0" x2="1" y2="0">
        <stop offset="0" stop-color="#ffffff"/>
        <stop offset="0.55" stop-color="#e3f3f6"/>
        <stop offset="1" stop-color="#b9e1e9"/>
      </linearGradient>
      <linearGradient id="panelTop" x1="0" y1="0" x2="0" y2="1">
        <stop offset="0" stop-color="#ffffff" stop-opacity="1"/>
        <stop offset="0.35" stop-color="#ffffff" stop-opacity="0"/>
      </linearGradient>
      <linearGradient id="waveDeep" x1="0" y1="0" x2="0" y2="1">
        <stop offset="0" stop-color="#8fd2de"/>
        <stop offset="1" stop-color="#2fa9bf"/>
      </linearGradient>
      <linearGradient id="waveWhite" x1="0" y1="0" x2="1" y2="0">
        <stop offset="0" stop-color="#ffffff"/>
        <stop offset="1" stop-color="#ffffff" stop-opacity="0.7"/>
      </linearGradient>
    </defs>
    <!-- backdrop panel -->
    <rect x="0" y="141" width="778" height="480" fill="url(#panelFade)"/>
    <rect x="0" y="141" width="778" height="480" fill="url(#panelTop)"/>
    <!-- right water block -->
    <rect x="778" y="460" width="422" height="260" fill="url(#waveDeep)"/>
    <!-- wave layers -->
    <path d="M760 500 C860 470 980 455 1200 480 L1200 520 C1040 505 900 515 760 540 Z" fill="#ffffff"/>
    <path d="M0 565 C200 560 420 570 620 545 C800 522 980 525 1200 560 L1200 600 C980 575 800 580 620 600 C420 620 200 610 0 600 Z" fill="url(#waveWhite)"/>
    <path d="M0 600 C220 620 420 640 640 615 C860 590 1020 595 1200 620 L1200 814 L0 814 Z" fill="url(#waveDeep)"/>
    <path d="M0 640 C240 680 520 690 760 660 C940 640 1080 645 1200 660 L1200 690 C1060 680 920 685 760 700 C520 725 260 715 0 690 Z" fill="#ffffff" opacity="0.85"/>
    <path d="M0 720 C300 760 620 740 900 715 C1020 705 1120 708 1200 715 L1200 814 L0 814 Z" fill="#3aafc3"/>
    <path d="M380 760 C620 735 860 720 1200 740 L1200 755 C880 745 640 760 380 775 Z" fill="#ffffff" opacity="0.7"/>
  </svg>

  <div class="flyer__sofa-photo" role="img" aria-label="Photo of a mint green sofa with six plush toys sitting on it: rabbit, whale, lion, penguin, bird and chick"></div>
  <div class="flyer__sofa-reflection" role="img" aria-label="Soft reflection of the sofa in the water"></div>

  <section class="brand">
    <div class="brand__mark">
      <span class="brand__dot"></span>
      <span class="brand__name">Seafolk Toys</span>
    </div>
    <p class="brand__tagline">Have you been there?</p>
  </section>
</main>
</body>
</html>
```